Designing business cards for my start-up business

The company is called Pellion. We are a start-up tech data company based in Guernsey, Channel Islands. We want the business cards to look clean, fresh and innovative, just what a tech company should be. We do not want the business cards to look corporate or too official such as a bank. I would like the front of the business card to have our logo and the tag line of "connecting talent". On the back will be our contact details, emails etc. However I am open to your ideas and suggestions. I have provided all our logos and a word doc of all our contact details. There are 4 directors of the business, so I want 4 versions of the same design.

Target Market(s)

Our clients are businesses of all industries. Its a broad target market.

Industry/Entity Type

Information Technology

Contact Information for Business Card

I have attached a word doc called "Business Cards info" which gives all contact details of the 4 employees for the company.

Requirements
Must have
• We must have our logo and the tag line of "connecting talent". This could on the front of the card and then the individuals contact details on the back. Other than that, I'm happy for the designers to come up with ideas/styles.
Nice to have
• N/A
Should not have
• I don't want the cards to look too formal or corporate. As mentioned, we are a tech start-up so we want to look innovative.

```html
<!DOCTYPE html>
<html lang="en">
<head>
<meta charset="utf-8">
<title>Pellion business cards</title>
<link href="https://fonts.googleapis.com/css2?family=Open+Sans:wght@400;600;700&display=swap" rel="stylesheet">
<style>
  :root {
    --stage: #2f2b29;
    --card-dark: #1b1b1b;
    --orange: #f4552f;
    --orange-deep: #c9302a;
    --white: #ffffff;
    --silver: #d9d9d9;
    --ink-soft: #e6e6e6;
  }
  html, body {
    margin: 0;
    width: 1200px;
    height: 780px;
    overflow: hidden;
    background: var(--stage);
    font-family: "Open Sans", Arial, sans-serif;
  }
  .stage {
    position: relative;
    width: 1200px;
    height: 780px;
  }
  .card {
    position: absolute;
    top: 235px;
    width: 535px;
    height: 306px;
    overflow: hidden;
    box-shadow: 0 12px 30px rgba(0,0,0,0.45);
  }
  /* Front */
  .card-front {
    left: 40px;
    background: linear-gradient(90deg, var(--orange-deep), var(--orange));
  }
  .front-band {
    position: absolute;
    inset: 0;
  }
  .front-brand {
    position: absolute;
    right: 22px;
    bottom: 26px;
    display: flex;
    gap: 8px;
    writing-mode: vertical-rl;
    transform: rotate(180deg);
  }
  .front-name {
    display: flex;
    align-items: center;
    gap: 14px;
    color: var(--white);
    font-weight: 700;
    font-size: 34px;
    line-height: 1;
    letter-spacing: 0.3em;
  }
  .mark-square {
    width: 26px;
    height: 26px;
    background: var(--white);
  }
  .front-tagline {
    order: -1;
    color: var(--white);
    font-weight: 600;
    font-size: 12px;
    line-height: 1;
    letter-spacing: 0.28em;
    text-transform: uppercase;
    padding-bottom: 40px;
  }
  /* Back */
  .card-back {
    left: 625px;
    background: var(--card-dark);
    color: var(--white);
  }
  .brand-block {
    position: absolute;
    left: 26px;
    top: 34px;
    width: 200px;
  }
  .brand-square {
    width: 186px;
    height: 186px;
    background: linear-gradient(135deg, var(--silver) 0 38%, var(--orange-deep) 38%, var(--orange) 100%);
  }
  .brand-name {
    margin-top: 18px;
    font-weight: 700;
    font-size: 24px;
    letter-spacing: 0.42em;
    color: var(--white);
  }
  .divider {
    position: absolute;
    left: 238px;
    top: 30px;
    width: 1px;
    height: 246px;
    background: var(--ink-soft);
  }
  .person {
    position: absolute;
    left: 258px;
    top: 40px;
  }
  .person-name {
    margin: 0;
    font-weight: 400;
    font-size: 30px;
    line-height: 1.1;
    color: var(--orange);
  }
  .person-role {
    margin: 2px 0 0;
    font-size: 14px;
    color: var(--ink-soft);
  }
  .contact-list {
    position: absolute;
    left: 258px;
    top: 156px;
    margin: 0;
    padding: 0;
    list-style: none;
    font-size: 12.5px;
    line-height: 1.45;
    color: var(--ink-soft);
  }
  .contact-list li {
    display: flex;
    align-items: flex-start;
    gap: 10px;
    margin-bottom: 4px;
  }
  .contact-icon {
    flex: none;
    width: 12px;
    height: 12px;
    margin-top: 3px;
  }
</style>
</head>
<body>
<main class="stage">

  <section class="card card-front" aria-label="Card front">
    <svg class="front-band" viewBox="0 0 535 306" preserveAspectRatio="none" aria-hidden="true">
      <polygon points="0,0 535,0 535,40 0,180" fill="#ffffff"/>
    </svg>
    <div class="front-brand">
      <div class="front-name">
        <span class="mark-square"></span>
        <span>Pellion</span>
      </div>
      <p class="front-tagline">connecting talent</p>
    </div>
  </section>

  <section class="card card-back" aria-label="Card back">
    <div class="brand-block">
      <div class="brand-square"></div>
      <div class="brand-name">Pellion</div>
    </div>
    <div class="divider"></div>

    <div class="person">
      <h1 class="person-name">Aled Morvan</h1>
      <p class="person-role">Director</p>
    </div>

    <ul class="contact-list">
      <li>
        <svg class="contact-icon" viewBox="0 0 12 12" aria-hidden="true"><rect width="12" height="12" fill="#f4552f"/><circle cx="6" cy="6" r="3.3" fill="none" stroke="#1b1b1b" stroke-width="1"/><line x1="2.7" y1="6" x2="9.3" y2="6" stroke="#1b1b1b" stroke-width="0.8"/></svg>
        <span>www.pellion-data.gg</span>
      </li>
      <li>
        <svg class="contact-icon" viewBox="0 0 12 12" aria-hidden="true"><rect width="12" height="12" fill="#f4552f"/><path d="M3.5 2.5 L5 2.5 L5.5 4.5 L4.6 5.2 Q5.5 7 6.8 7.4 L7.5 6.5 L9.5 7 L9.5 8.5 Q6 9.5 3.5 5.5 Z" fill="#1b1b1b"/></svg>
        <span>+44 7700 418 562</span>
      </li>
      <li>
        <svg class="contact-icon" viewBox="0 0 12 12" aria-hidden="true"><rect width="12" height="12" fill="#f4552f"/><rect x="2.5" y="3.5" width="7" height="5" fill="none" stroke="#1b1b1b" stroke-width="0.9"/><polyline points="2.5,3.5 6,6.3 9.5,3.5" fill="none" stroke="#1b1b1b" stroke-width="0.9"/></svg>
        <span>aled.morvan@pellion-data.gg</span>
      </li>
      <li>
        <svg class="contact-icon" viewBox="0 0 12 12" aria-hidden="true"><rect width="12" height="12" fill="#f4552f"/><path d="M6 10 L3.6 5.8 A2.7 2.7 0 1 1 8.4 5.8 Z" fill="#1b1b1b"/><circle cx="6" cy="4.6" r="1" fill="#f4552f"/></svg>
        <span>12 Rue du Marché, St Peter Port<br>Guernsey, GY1 4QX, Channel Islands</span>
      </li>
    </ul>
  </section>

</main>
</body>
</html>
```